Painting Company Business Card

Brightwell Painting needs a new business card. See attachments for our logo and current card as an example.
We want to utilize the same colors in the logo, and keep all the information that is currently on it. Just need an updated and modern design.
We are open to loosing the Association Logos if it means a better design.
We are also entertaining a spot for a picture of a headshot of the person listed on the card. Head shot can be finished later.

```html
<!DOCTYPE html>
<html lang="en">
<head>
<meta charset="utf-8">
<title>Brightwell Painting – Business Card</title>
<link href="https://fonts.googleapis.com/css2?family=Source+Sans+3:wght@400;600&display=swap" rel="stylesheet">
<style>
  :root {
    --backdrop: #c8cdd0;
    --card: #f7f7f7;
    --forest: #3a3f2c;
    --maroon: #5e3431;
    --ink: #3a3f2c;
    --white: #ffffff;
  }
  * { margin: 0; padding: 0; box-sizing: border-box; }
  html, body {
    width: 1200px; height: 1200px; overflow: hidden;
    background: var(--backdrop);
    font-family: "Source Sans 3", sans-serif;
  }
  .card {
    position: absolute; left: 250px;
    width: 700px; height: 400px;
    background: var(--card);
    overflow: hidden;
  }
  .card--front { top: 146px; }
  .card--back { top: 652px; }

  /* Front */
  .brand-mark {
    position: absolute; left: 0; right: 0; top: 0; bottom: 0;
    display: flex; align-items: center; justify-content: center; gap: 22px;
  }
  .brand-mark__square {
    width: 34px; height: 34px; background: var(--forest);
  }
  .brand-mark__name {
    color: var(--forest); font-weight: 600;
    font-size: 48px; line-height: 1.05; letter-spacing: 0.5px;
  }

  /* Back */
  .person {
    position: absolute; left: 36px; top: 38px;
    border-left: 6px solid var(--forest);
    padding-left: 8px; color: var(--ink);
  }
  .person__name { font-size: 30px; line-height: 32px; }
  .person__role { font-size: 19px; line-height: 22px; }

  .contact {
    position: absolute; left: 36px; top: 150px;
    list-style: none; color: var(--ink); font-size: 21px;
  }
  .contact li { display: flex; align-items: center; gap: 6px; height: 45px; }
  .contact svg { width: 26px; height: 26px; flex: none; }

  .services {
    position: absolute; left: 48px; top: 282px;
    display: grid; grid-template-columns: 180px 200px; row-gap: 6px;
    list-style: none; color: var(--ink); font-size: 21px;
  }
  .services li { position: relative; padding-left: 22px; }
  .services li::before {
    content: ""; position: absolute; left: 0; top: 12px;
    width: 6px; height: 6px; border-radius: 50%; background: var(--ink);
  }

  .corner { position: absolute; left: 0; top: 0; width: 700px; height: 400px; }
  .corner-name {
    position: absolute; right: 20px; bottom: 32px;
    color: var(--white); font-weight: 600; font-size: 17px;
    line-height: 1.1; text-align: right;
  }
</style>
</head>
<body>

<section class="card card--front">
  <div class="brand-mark">
    <span class="brand-mark__square"></span>
    <div class="brand-mark__name">Brightwell<br>Painting</div>
  </div>
</section>

<section class="card card--back">
  <div class="person">
    <div class="person__name">Daniel Reyes</div>
    <div class="person__role">Manager</div>
  </div>

  <ul class="contact">
    <li>
      <svg viewBox="0 0 24 24" aria-hidden="true"><path fill="var(--forest)" d="M6.6 10.8a15.1 15.1 0 0 0 6.6 6.6l2.2-2.2c.3-.3.7-.4 1-.2 1.1.4 2.3.6 3.6.6.6 0 1 .4 1 1V20c0 .6-.4 1-1 1A17 17 0 0 1 3 4c0-.6.4-1 1-1h3.5c.6 0 1 .4 1 1 0 1.3.2 2.5.6 3.6.1.3 0 .7-.2 1z"/></svg>
      262-555-0148
    </li>
    <li>
      <svg viewBox="0 0 24 24" aria-hidden="true" fill="none" stroke="var(--forest)" stroke-width="1.5"><rect x="2" y="5" width="20" height="14"/><path d="M2 5l10 8 10-8M2 19l7-7M22 19l-7-7"/></svg>
      Daniel.Brightwell@mailbox.com
    </li>
    <li>
      <svg viewBox="0 0 24 24" aria-hidden="true" fill="none" stroke="var(--forest)" stroke-width="1.3"><circle cx="12" cy="12" r="10"/><ellipse cx="12" cy="12" rx="4.5" ry="10"/><path d="M2 12h20M4 6.5h16M4 17.5h16M12 2v20"/></svg>
      BrightwellPainting.com
    </li>
  </ul>

  <ul class="services">
    <li>Exterior Painting</li>
    <li>Interior Painting</li>
    <li>Carpentry</li>
    <li>Drywall</li>
  </ul>

  <svg class="corner" viewBox="0 0 700 400" aria-hidden="true">
    <polygon points="700,168 700,400 450,400" fill="var(--forest)"/>
    <polygon points="700,292 700,400 610,400" fill="var(--maroon)"/>
  </svg>
  <div class="corner-name">Brightwell<br>Painting</div>
</section>

</body>
</html>
```